Brookfield Corner Mart - Collateral
Marketing Collateral
Project: Brookfield Corner Mart - Collateral
Brookfield Corner Mart - Collateral -
Creative Brief
Retail customers
Need to focus on Cigars, Beer and Wine. Also need to focus the tax free aspect for customers due to no sales tax in New Hampshire.

```html
<!DOCTYPE html>
<html lang="en">
<head>
<meta charset="utf-8">
<title>Brookfield Corner Mart – Tri-fold Brochure</title>
<link rel="stylesheet" href="https://fonts.googleapis.com/css2?family=Open+Sans:wght@400;600;700&display=swap">
<style>
  :root {
    --backdrop: #c9b08e;
    --label: #ffffff;
    --maroon: #8b2b31;
    --maroon-deep: #6e1f25;
    --brown: #7a5232;
    --paper: #ffffff;
    --ink: #555555;
    --ink-light: #f3e9e2;
    --cigar-dark: #4a2a14;
    --cigar-mid: #9a6a3c;
    --cigar-light: #d9b58a;
  }
  * { box-sizing: border-box; margin: 0; padding: 0; }
  html, body { width: 1200px; height: 1052px; overflow: hidden; }
  body {
    background: var(--backdrop);
    font-family: "Open Sans", Arial, sans-serif;
    color: var(--ink);
  }
  .sheet { position: absolute; left: 210px; width: 780px; }
  .sheet--outside { top: 14px; }
  .sheet--inside { top: 546px; }
  .panel-labels { display: flex; height: 34px; align-items: center; }
  .panel-labels span {
    width: 260px; text-align: center; color: var(--label);
    font-weight: 600; font-size: 20px;
  }
  .spread {
    display: flex; height: 458px;
    box-shadow: 0 4px 14px rgba(60, 40, 20, 0.35);
  }
  .panel { width: 260px; height: 100%; position: relative; overflow: hidden; }
  .panel--white { background: var(--paper); }
  .panel--maroon { background: var(--maroon); color: var(--ink-light); }
  .panel--brown { background: var(--brown); color: var(--ink-light); }

  /* letter panel */
  .letter { padding: 28px 24px; font-size: 8.5px; line-height: 1.55; }
  .letter p { margin-bottom: 11px; }

  /* name block in place of the mark */
  .brand {
    display: flex; align-items: center; justify-content: center; gap: 10px;
  }
  .brand-dot {
    width: 40px; height: 40px; border-radius: 50%;
    background: var(--maroon); flex: none;
  }
  .brand-name {
    font-weight: 700; font-size: 15px; line-height: 1.15;
    letter-spacing: 1px; text-transform: uppercase; color: var(--maroon);
  }
  .panel--maroon .brand-dot { background: var(--ink-light); }
  .panel--maroon .brand-name { color: var(--ink-light); }

  .back-brand { position: absolute; top: 232px; left: 0; right: 0; }
  .address {
    position: absolute; top: 320px; left: 0; right: 0;
    text-align: center; font-size: 14px; line-height: 1.35; color: #fff;
  }
  .address .web { font-size: 10px; }

  .front-brand { position: absolute; top: 0; left: 0; right: 0; height: 176px; }
  .photo { position: absolute; left: 0; right: 0; }
  .photo--cigars-front {
    top: 176px; bottom: 0;
    background: radial-gradient(ellipse at 60% 55%, var(--cigar-light), var(--cigar-mid) 45%, var(--cigar-dark));
  }

  /* inside */
  .copy { position: absolute; left: 18px; right: 18px; font-size: 8px; line-height: 1.55; }
  .copy h3 { font-size: 10px; font-weight: 700; margin-bottom: 6px; }
  .copy p { margin-bottom: 6px; }
  .panel--white .copy h3 { color: #333; }
  .panel--maroon .copy h3, .panel--brown .copy h3 { color: #fff; }

  .photo--wine-cellar {
    top: 150px; height: 150px;
    background: linear-gradient(135deg, #2a1410, #6b3a26 45%, #3a2018);
  }
  .photo--beer {
    top: 300px; bottom: 0;
    background: radial-gradient(ellipse at 50% 45%, #f0b24a, #b5651e 45%, #3a1a0c);
  }
  .photo--cigar-box {
    top: 0; height: 150px;
    background: linear-gradient(120deg, #5a3318, #a8743f 50%, #c9925a 70%, #6a3a1c);
  }
</style>
</head>
<body>

<section class="sheet sheet--outside">
  <div class="panel-labels"><span>Inside Fold</span><span>Back</span><span>Front</span></div>
  <div class="spread">
    <div class="panel panel--white letter">
      <p>Dear Neighbor,</p>
      <p>Thank you for stopping by our corner store. We stock hand rolled cigars, cold craft beer and a wide range of fine wines for every taste.</p>
      <p>New Hampshire has no sales tax, so every bottle and every box costs exactly the price on the shelf.</p>
      <p>Our humidor is kept at ideal levels year round, and our staff can help you find a new favorite.</p>
      <p>Ask about monthly tastings and member savings on cases of wine and beer.</p>
      <p>We look forward to seeing you soon.</p>
      <p>The Brookfield Team</p>
    </div>
    <div class="panel panel--maroon">
      <div class="brand back-brand">
        <span class="brand-dot"></span>
        <span class="brand-name">Brookfield<br>Corner Mart</span>
      </div>
      <div class="address">
        Address here,<br>Lorem, Ipsum 12345<br>Lorem Ipsum<br><span class="web">www.website.com</span>
      </div>
    </div>
    <div class="panel panel--white">
      <div class="brand front-brand">
        <span class="brand-dot"></span>
        <span class="brand-name">Brookfield<br>Corner Mart</span>
      </div>
      <div class="photo photo--cigars-front" role="img" aria-label="Close-up photo of stacked hand rolled cigars"></div>
    </div>
  </div>
</section>

<section class="sheet sheet--inside">
  <div class="panel-labels"><span>Inside 1</span><span>Inside 2</span><span>Inside 3</span></div>
  <div class="spread">
    <div class="panel panel--maroon">
      <div class="copy" style="top:18px">
        <h3>Fine Wines</h3>
        <p>Reds, whites and sparkling bottles from vineyards near and far, chosen for value and flavor.</p>
        <p>Staff picks change every week, with notes on each label to guide you.</p>
      </div>
      <div class="photo photo--wine-cellar" role="img" aria-label="Photo of wine bottles resting in a cellar rack"></div>
      <div class="copy" style="top:318px">
        <h3>Cellar Club</h3>
        <p>Join free and save on mixed cases of six or more bottles all year.</p>
      </div>
    </div>
    <div class="panel panel--white">
      <div class="copy" style="top:18px">
        <h3>Premium Cigars</h3>
        <p>Our walk in humidor holds a broad selection of hand rolled cigars from trusted makers.</p>
        <p>Cutters, lighters and cases are on hand too.</p>
      </div>
      <div class="copy" style="top:168px">
        <h3>Cold Craft Beer</h3>
        <p>Local brews and imports fill our coolers, with singles you can mix into your own pack.</p>
      </div>
      <div class="photo photo--beer" role="img" aria-label="Photo of glasses of craft beer on a bar"></div>
    </div>
    <div class="panel panel--brown">
      <div class="photo photo--cigar-box" role="img" aria-label="Photo of cigars in an open box beside a glass of brandy"></div>
      <div class="copy" style="top:168px">
        <h3>Tax Free Savings</h3>
        <p>New Hampshire charges no sales tax, so the price you see is the price you pay.</p>
        <p>Visitors from nearby states save on every cigar, bottle and case.</p>
      </div>
      <div class="copy" style="top:318px">
        <h3>Visit Us</h3>
        <p>Open seven days with easy parking right out front.</p>
      </div>
    </div>
  </div>
</section>

</body>
</html>
```